Design a Food Label Card for Matcha Tea Product

The task is to design a food label card for a Matcha product. Design guidelines are found in the attached document. The logo to be used is also found in the attached document.
__________________________________________________________________

Food Label Packaging Design Guidelines
The food label packaging design is made for ceremonial grade organic Japanese Matcha tea. The tea would be stored in a cylindrical aluminum/tin packaging of the following dimensions 16 cm (horizontal) x 18 cm (vertical) of 100g weight.

Design guidelines:
1) Brand name: TOLVEN
2) Product name: Organic Matcha
3) Food ingredient: Ceremonial Grade Japanese Matcha
4) Production & expiration date: place it somewhere on the label (may be removed)
5) Name of Distributer: Tolven Leaf Tea Trading
6) Net Weight: 100g
7) Country of Origin: Japan
8) Barcode: Please add a space for barcode
9) Storage Condition: Keep refrigerated
10) Complete Address of Manfucturer: Please add a dummy address for design purposes

Target Market(s)

Mostly business to business such as suppliers, cafes etc.

Industry/Entity Type

Coffee Shop

Font styles to use
Sans Serif

Colors

Designer to choose colors to be used in the design.

Requirements
Must have
• The same color as the designed logo.
Nice to have
• Modern design and elegant design.
Should not have
• multiple colors.

```html
<!DOCTYPE html>
<html lang="en">
<head>
<meta charset="utf-8">
<title>Tolven Organic Matcha Label</title>
<link rel="stylesheet" href="https://fonts.googleapis.com/css2?family=Source+Code+Pro:wght@400;600;700&family=Source+Sans+3:wght@300;400;600;700&display=swap">
<style>
  :root {
    --teal: #25a89f;
    --white: #ffffff;
    --mono: "Source Code Pro", monospace;
    --sans: "Source Sans 3", sans-serif;
  }
  html, body { margin: 0; padding: 0; overflow: hidden; }
  .label {
    position: relative;
    width: 1200px;
    height: 985px;
    background: var(--teal);
    color: var(--teal);
    overflow: hidden;
  }
  .panel { position: absolute; left: 42px; width: 1117px; background: var(--white); }
  .panel--top { top: 42px; height: 397px; }
  .panel--bottom { top: 538px; height: 404px; }

  .brand {
    position: absolute; left: 0; right: 0; top: 196px;
    display: flex; align-items: center; justify-content: center; gap: 14px;
    font-family: var(--sans); font-weight: 600; font-size: 52px; letter-spacing: 4px;
    color: var(--teal);
  }
  .brand__dot { width: 14px; height: 14px; border-radius: 50%; background: var(--teal); }

  .product-title {
    position: absolute; left: 0; right: 0; top: 439px; height: 99px;
    margin: 0; display: flex; align-items: center; justify-content: center;
    font-family: var(--mono); font-weight: 700; font-size: 82px; letter-spacing: 28px;
    color: var(--white); padding-left: 28px;
  }

  .info { position: absolute; left: 0; right: 0; top: 263px; bottom: 0; border-top: 1.5px solid var(--teal); }
  .info__row1 { position: absolute; left: 0; right: 0; top: 0; height: 45px; border-bottom: 1.5px solid var(--teal); }
  .ingredients {
    position: absolute; left: 8px; top: 0; width: 682px; height: 45px;
    display: flex; align-items: center; font-family: var(--sans); font-weight: 300; font-size: 22.5px; white-space: nowrap;
    border-right: 1.5px solid var(--teal);
  }
  .ingredients strong { font-weight: 700; margin-right: 5px; }
  .storage {
    position: absolute; left: 690px; right: 0; top: 0; height: 45px;
    display: flex; align-items: center; justify-content: center;
    font-family: var(--sans); font-size: 22.5px;
  }

  .cell { position: absolute; top: 46px; bottom: 0; font-family: var(--mono); font-size: 13px; letter-spacing: 1.5px; }
  .cell--dates { left: 0; width: 287px; border-right: 1.5px solid var(--teal); }
  .cell--dates p { position: absolute; left: 8px; margin: 0; }
  .cell--distributor { left: 287px; width: 222px; border-right: 1.5px solid var(--teal); text-align: center; }
  .cell--distributor p { position: absolute; left: 0; right: 0; margin: 0; }
  .cell--address { left: 509px; width: 236px; border-right: 1.5px solid var(--teal); padding: 10px 0 0 13px; box-sizing: border-box; line-height: 19.3px; }
  .cell--address p { margin: 0; }
  .bold { font-weight: 700; }
  .cell--weight { left: 745px; width: 167px; border-right: 1.5px solid var(--teal); font-family: var(--sans); letter-spacing: 0; text-align: center; }
  .origin { height: 23px; border-bottom: 1.5px solid var(--teal); font-size: 13px; line-height: 23px; }
  .origin strong { font-weight: 600; }
  .net { font-weight: 600; font-size: 26px; line-height: 34px; margin-top: 6px; }
  .cell--barcode { left: 912px; right: 0; }
</style>
</head>
<body>
<div class="label">
  <section class="panel panel--top">
    <div class="brand"><span class="brand__dot"></span>TOLVEN</div>
  </section>

  <h1 class="product-title">ORGANIC MATCHA</h1>

  <section class="panel panel--bottom">
    <div class="info">
      <div class="info__row1">
        <div class="ingredients"><strong>Ingredients:</strong> 100% Organic Ceremonial Grade Japanese Matcha</div>
        <div class="storage">KEEP REFRIGERATED</div>
      </div>

      <div class="cell cell--dates">
        <p style="top:25px">Date of Production:</p>
        <p style="top:63px">Expiration Date:</p>
      </div>
      <div class="cell cell--distributor">
        <p class="bold" style="top:29px">Distributed by:</p>
        <p style="top:57px">Tolven Leaf Tea Trading</p>
      </div>
      <div class="cell cell--address">
        <p class="bold">Tolven Leaf Tea Trading</p>
        <p>Lorem ipsum dolor sit,</p>
        <p>Amet consectetuer,</p>
        <p>Adipiscing elit, sed</p>
      </div>
      <div class="cell cell--weight">
        <div class="origin"><strong>Country of Origin:</strong> Japan</div>
        <div class="net">Net Weight:<br>100g</div>
      </div>
      <div class="cell cell--barcode"></div>
    </div>
  </section>
</div>
</body>
</html>
```